Business card design for Automotive workshop

We need a business card for a new automotive repair and tyre shop called Ridgeback Prime Automotive located in New Zealand. We are a clean, modern and fresh workshop and company.

Front needs to feature logo,
my name:
Lachie Westergaard (director)

Address:
48 Marlow Lane
Whitianga 3510

Phone: 07 842 1937
Mobile: 027 519 2764
Email: office@ridgebackmotors.co.nz
Website: ridgebackmotors.co.nz

Back needs to feature an area to write down appointment details, date and time.

Also feature a list of jobs and work we do such as,
Vehicle Servicing
All Mechanical Repairs
Warrant of Fitness
Tyres & Wheel Alignments
Automotive Diagnostics
Automotive Parts & Supplies

```html
<!DOCTYPE html>
<html lang="en">
<head>
<meta charset="utf-8">
<title>Ridgeback Prime Automotive – Business Card</title>
<link href="https://fonts.googleapis.com/css2?family=Open+Sans:wght@400;600;700&family=Roboto:wght@400;500;700&display=swap" rel="stylesheet">
<style>
  :root {
    --red: #e3141f;
    --black: #141414;
    --card-dark: #1c1c1c;
    --white: #ffffff;
    --ink: #222222;
    --muted: #5a5a5a;
    --bg: #d9d9d9;
    --dots: #9a9a9a;
  }
  * { box-sizing: border-box; margin: 0; padding: 0; }
  html, body { width: 1200px; height: 960px; overflow: hidden; }
  body {
    background: var(--bg);
    position: relative;
    font-family: "Open Sans", Arial, sans-serif;
  }
  .card {
    position: absolute;
    width: 560px;
    height: 320px;
    overflow: hidden;
    box-shadow: 0 10px 28px rgba(0,0,0,0.25);
  }

  /* Back side */
  .card-back {
    left: 60px; top: 100px;
    background: var(--card-dark);
    color: var(--white);
    font-family: "Roboto", Arial, sans-serif;
  }
  .back-brand {
    position: absolute; top: 34px; left: 0; right: 0;
    display: flex; justify-content: center; align-items: center; gap: 12px;
  }
  .brand-mark {
    width: 16px; height: 16px; background: var(--red);
  }
  .back-brand .brand-name {
    font-size: 27px; font-weight: 700; letter-spacing: 1px;
    text-transform: uppercase; color: #cfcfcf;
  }
  .services {
    position: absolute; top: 92px; left: 0; right: 0; text-align: center;
  }
  .services-title {
    color: var(--red); font-size: 19px; font-weight: 700;
    text-transform: uppercase; letter-spacing: 0.5px; margin-bottom: 6px;
  }
  .services-line { font-size: 14.5px; line-height: 21px; font-weight: 500; }
  .bullet { color: var(--red); margin: 0 5px; }
  .appointment {
    position: absolute; left: 0; right: 0; bottom: 24px; height: 100px;
    background: var(--white);
    padding: 22px 28px 0;
  }
  .appt-row {
    display: flex; align-items: baseline; gap: 6px;
    font-size: 14px; font-weight: 500; color: var(--red); margin-bottom: 20px;
  }
  .appt-line { flex: 1; border-bottom: 1.5px dotted var(--dots); height: 1px; }
  .appt-line.date { flex: 1.3; }

  /* Front side */
  .card-front {
    left: 580px; top: 540px;
    background: var(--white);
    color: var(--ink);
  }
  .front-brand {
    position: absolute; left: 40px; top: 132px;
    display: flex; align-items: center; gap: 10px;
  }
  .front-brand .brand-name {
    font-size: 22px; font-weight: 700; color: var(--red);
    text-transform: uppercase; letter-spacing: 0.5px; line-height: 1.15;
  }
  .contact {
    position: absolute; left: 320px; top: 58px;
  }
  .person-name {
    color: var(--red); font-size: 18px; font-weight: 600;
    text-transform: uppercase; letter-spacing: 0.3px;
  }
  .person-role { font-size: 14px; color: var(--ink); margin-bottom: 12px; }
  .contact-item {
    display: flex; align-items: center; gap: 7px;
    font-size: 12.5px; color: var(--muted); line-height: 20px;
  }
  .contact-item svg { width: 11px; height: 11px; flex: none; }
  .icon-spacer { width: 11px; flex: none; }
  .band-red {
    position: absolute; left: 0; bottom: 0; width: 300px; height: 28px;
    background: var(--red);
  }
  .band-black {
    position: absolute; left: 300px; bottom: 28px; right: 0; height: 40px;
    background: var(--black); color: var(--white);
    display: flex; align-items: center; justify-content: flex-end;
    padding-right: 22px; font-size: 14px; letter-spacing: 0.3px;
  }
  .band-black-tail {
    position: absolute; left: 300px; bottom: 0; right: 0; height: 28px;
    background: var(--white);
  }
</style>
</head>
<body>

<section class="card card-back">
  <div class="back-brand">
    <span class="brand-mark"></span>
    <span class="brand-name">Ridgeback Prime Automotive</span>
  </div>
  <div class="services">
    <p class="services-title">Vehicle Servicing</p>
    <p class="services-line">All Mechanical Repairs<span class="bullet">•</span>Warrant of Fitness<span class="bullet">•</span>Tyres &amp; Wheel Alignments</p>
    <p class="services-line">Automotive Diagnostics<span class="bullet">•</span>Automotive Parts &amp; Supplies</p>
  </div>
  <div class="appointment">
    <div class="appt-row"><span>Date:</span><span class="appt-line date"></span><span>Time:</span><span class="appt-line"></span></div>
    <div class="appt-row"><span>Date:</span><span class="appt-line date"></span><span>Time:</span><span class="appt-line"></span></div>
  </div>
</section>

<section class="card card-front">
  <div class="front-brand">
    <span class="brand-name">Ridgeback Prime<br>Automotive</span>
  </div>
  <div class="contact">
    <p class="person-name">Lachie Westergaard</p>
    <p class="person-role">Director</p>
    <p class="contact-item"><span class="icon-spacer"></span>48 Marlow Lane Whitianga 3510</p>
    <p class="contact-item">
      <svg viewBox="0 0 12 12" aria-hidden="true"><path fill="#e3141f" d="M2.6 0.8l1.8 2.1-1 1.2c0.7 1.5 1.8 2.6 3.3 3.3l1.2-1 2.1 1.8-0.9 2C5.2 9.8 2 6.7 0.6 1.7z"/></svg>
      07 842 1937
    </p>
    <p class="contact-item">
      <svg viewBox="0 0 12 12" aria-hidden="true"><rect x="3" y="0.8" width="6" height="10.4" rx="1" fill="none" stroke="#e3141f" stroke-width="1.4"/><circle cx="6" cy="9.2" r="0.7" fill="#e3141f"/></svg>
      027 519 2764
    </p>
    <p class="contact-item">
      <svg viewBox="0 0 12 12" aria-hidden="true"><rect x="0.8" y="2.5" width="10.4" height="7" fill="#e3141f"/><path d="M0.8 2.5L6 6.6 11.2 2.5" fill="none" stroke="#fff" stroke-width="1"/></svg>
      office@ridgebackmotors.co.nz
    </p>
  </div>
  <div class="band-red"></div>
  <div class="band-black">www.ridgebackmotors.co.nz</div>
  <div class="band-black-tail"></div>
</section>

</body>
</html>
```